Brochure Design Project for Custom Embroidery (Monograms) Shop

The need is for an 8.5” x 11” single sheet (might be front and back, as required) to promote our company. Bee’s Stitchery, LLC provides personalization (monogramming) services as well as the items themselves, for business owners and consumers. Our company currently provides:
- Hats, Visors, Tee Shirts, Polo and Dress Shirts, Sweatshirts, Hoodies, Sports Wear (team clothing) Shorts and Shirts, etc
- Canvas Bags and Totes, Fleece Blankets and Throws, Backpacks, Reusable Grocery Bags, etc
- Men’s and Women’s zippered jackets, pull over jackets, Fleece jackets
- Children’s Shirts, Bibs, Towels
- Will work with customer’s current custom Logo
- Will work with customer to create new company logo
- Customer can view all items on website www.beesstitchery-example.com (new site coming soon….)
Project needs to speak to three main concepts 1) Embroidery name, initials and logo on items, 2) [heat] Transfer names, initials, logos and graphics on items and 3) custom logo work.
Target market for this brochure (although we’d like to have it a little bit generic for other uses, if possible) is brand new business owners who have just purchased equipment to start their own business. These folk are attending training classes and this brochure will be a part of the training section that has to do with ‘creating your business image and start some Brand recognition’. The trainer will speak to the importance of them creating their own company image and this brochure will be placed in their take home material.
Things we like:
- White space
- Pictures / graphics of items, product and people
- A spot to input the ‘current’ special
- Our Company Logo and colors (red green beige)
- Spot in the brochure for the ‘current special’
- References to the web site
- Suitable for 3 hole punch (attention to the left margin)
- Professional appearance
Things not so good:
- Dark gloomy backgrounds
- Very tiny small text
Target Market(s)
business men and women starting their own business (easy text swaps for general public would be a huge plus)
Industry/Entity Type
Training
Look and feel

```html
<!DOCTYPE html>
<html lang="en">
<head>
<meta charset="utf-8">
<title>Bee’s Stitchery – Make your brand recognizable</title>
<link rel="stylesheet" href="https://fonts.googleapis.com/css2?family=Maven+Pro:wght@400;500;700&display=swap">
<style>
  :root {
    --green: #2fa343;
    --green-dark: #3a8f34;
    --green-light: #73b654;
    --red: #e0202f;
    --red-dark: #b8141f;
    --white: #ffffff;
    --ink: #2a2a2a;
    --grey: #5a5a5a;
  }
  * { box-sizing: border-box; margin: 0; padding: 0; }
  html, body { width: 925px; height: 1200px; overflow: hidden; }
  body {
    position: relative;
    background: var(--white);
    font-family: "Maven Pro", sans-serif;
    color: var(--ink);
  }
  .headline {
    position: absolute; left: 150px; top: 82px;
    font-size: 47px; font-weight: 400; line-height: 52px;
    letter-spacing: -0.3px;
  }
  .headline .line-green { color: var(--green); display: block; }
  .headline .line-red { color: var(--red); display: block; }
  .brand-name {
    position: absolute; left: 600px; top: 100px;
    display: flex; align-items: center; gap: 12px;
    font-size: 34px; font-weight: 500; color: var(--green);
  }
  .brand-name .dot {
    width: 28px; height: 28px; border-radius: 50%; background: var(--red);
  }
  .top-band {
    position: absolute; left: 0; top: 205px; width: 925px; height: 23px;
    background: linear-gradient(90deg, var(--red-dark), var(--red) 30%, var(--red) 70%, var(--red-dark));
  }
  .green-field { position: absolute; left: 0; top: 228px; }
  .hero-photo {
    position: absolute; left: 560px; top: 228px; width: 365px; height: 540px;
    background: linear-gradient(180deg, #d9545d 0%, #e7b7b3 38%, #f3eeea 62%, #c9303a 84%, rgba(255,255,255,0) 100%);
  }
  .services {
    position: absolute; left: 160px; top: 290px; color: var(--white);
  }
  .services h2 { font-size: 27px; font-weight: 700; margin-bottom: 40px; }
  .services ul { list-style: none; }
  .services li {
    position: relative; padding-left: 56px;
    font-size: 20px; line-height: 29px; margin-bottom: 26px; width: 380px;
  }
  .services li::before {
    content: ""; position: absolute; left: 0; top: 2px;
    width: 34px; height: 34px; border-radius: 50%;
    background: radial-gradient(circle, var(--red) 0 7px, var(--white) 8px);
    box-shadow: 0 1px 3px rgba(0,0,0,.3);
  }
  .special {
    position: absolute; left: 99px; top: 810px; width: 238px; height: 238px;
    border: 3px solid var(--red); border-radius: 12px;
  }
  .special-photo {
    position: absolute; left: 22px; top: 42px; width: 185px; height: 160px;
    background: radial-gradient(ellipse at 50% 45%, #5a5a5a, #1e1e1e 60%, rgba(255,255,255,0) 75%);
  }
  .special-ribbon {
    position: absolute; left: 118px; top: 790px; width: 215px; height: 46px;
    background: linear-gradient(180deg, #ef3340, var(--red-dark));
    color: var(--white); font-size: 23px; font-weight: 500;
    display: flex; align-items: center; justify-content: center;
    transform: rotate(-12deg); transform-origin: left center;
    border-radius: 3px;
  }
  .price { position: absolute; left: 252px; top: 930px; }
  .price span {
    position: absolute; inset: 0; display: flex; align-items: center; justify-content: center;
    color: var(--white); font-size: 30px; font-weight: 700;
  }
  .items { position: absolute; left: 395px; top: 770px; width: 480px; }
  .item {
    position: absolute; width: 120px; text-align: center;
    font-size: 11.5px; font-weight: 500; color: var(--ink); letter-spacing: .3px;
  }
  .item svg { display: block; margin: 0 auto 14px; }
  .more {
    position: absolute; width: 120px; text-align: center;
    color: var(--green); font-size: 21px; line-height: 22px;
  }
  .footer {
    position: absolute; left: 0; top: 1108px; width: 925px; text-align: center;
    font-size: 19px; color: var(--ink);
  }
  .footer a { color: var(--red); font-weight: 700; text-decoration: none; }
</style>
</head>
<body>

<h1 class="headline">
  <span class="line-green">Make your brand</span>
  <span class="line-red">recognizable</span>
</h1>

<div class="brand-name"><span class="dot"></span>Bee’s Stitchery</div>

<div class="top-band"></div>

<svg class="green-field" width="925" height="480" viewBox="0 0 925 480" aria-hidden="true">
  <defs>
    <linearGradient id="fieldGrad" x1="0" y1="0" x2="1" y2="1">
      <stop offset="0" stop-color="#52a541"/>
      <stop offset=".6" stop-color="#3b9236"/>
      <stop offset="1" stop-color="#2f8430"/>
    </linearGradient>
  </defs>
  <path d="M0 0 H925 V380 C760 385 460 400 0 472 Z" fill="url(#fieldGrad)"/>
</svg>

<div class="hero-photo" role="img" aria-label="Person in a red shirt carrying a white canvas tote with red trim, printed with a sample customer logo"></div>

<section class="services">
  <h2>Our services:</h2>
  <ul>
    <li>Embroidery name, initials and logo on items,</li>
    <li>Heat Transfer names, initials, logos and graphics on items</li>
    <li>Custom logo/design work.</li>
  </ul>
</section>

<div class="special">
  <div class="special-photo" role="img" aria-label="Black messenger bag with shoulder strap, the current special item"></div>
</div>
<div class="special-ribbon">current special</div>
<div class="price" style="width:104px;height:104px;">
  <svg width="104" height="104" viewBox="0 0 104 104" aria-hidden="true">
    <polygon fill="#e0202f" points="52,2 59,14 72,6 74,21 89,19 84,33 99,39 88,49 99,60 85,66 91,80 76,80 74,95 61,88 52,101 43,88 30,95 28,80 13,80 19,66 5,60 16,49 5,39 20,33 15,19 30,21 32,6 45,14"/>
  </svg>
  <span>$35</span>
</div>

<div class="items">
  <div class="item" style="left:0;top:0;">
    <svg width="80" height="66" viewBox="0 0 80 66"><path fill="#2fa343" d="M10 42 C10 14 30 6 46 6 C64 6 72 20 72 42 Z M0 42 H74 V50 H0 Z"/><circle cx="56" cy="28" r="8" fill="#fff"/><circle cx="56" cy="28" r="4" fill="#e0202f"/></svg>
    HATS
  </div>
  <div class="item" style="left:124px;top:0;">
    <svg width="80" height="66" viewBox="0 0 80 66"><path fill="#2fa343" d="M28 4 C32 10 48 10 52 4 L74 14 L68 28 L60 25 V62 H20 V25 L12 28 L6 14 Z"/><circle cx="40" cy="30" r="8" fill="#fff"/><circle cx="40" cy="30" r="4" fill="#e0202f"/></svg>
    T-SHIRTS
  </div>
  <div class="item" style="left:248px;top:0;">
    <svg width="80" height="66" viewBox="0 0 80 66"><path fill="#2fa343" d="M30 0 H50 C54 4 54 12 50 14 L70 20 L74 60 H64 L62 34 V64 H18 V34 L16 60 H6 L10 20 L30 14 C26 12 26 4 30 0 Z"/><circle cx="40" cy="36" r="8" fill="#fff"/><circle cx="40" cy="36" r="4" fill="#e0202f"/></svg>
    SPORTS WEAR
  </div>
  <div class="item" style="left:372px;top:0;">
    <svg width="80" height="66" viewBox="0 0 80 66"><path fill="#2fa343" d="M16 6 H64 L70 58 H46 L40 26 L34 58 H10 Z"/><circle cx="56" cy="40" r="7" fill="#fff"/><circle cx="56" cy="40" r="3.5" fill="#e0202f"/></svg>
    SHORTS
  </div>
  <div class="item" style="left:0;top:150px;">
    <svg width="80" height="66" viewBox="0 0 80 66"><path fill="#2fa343" d="M8 14 C20 6 44 4 60 10 L72 22 C74 36 70 52 62 58 H14 C8 48 6 30 8 14 Z"/><path fill="#fff" opacity=".35" d="M8 14 C24 18 44 18 60 10 L62 16 C44 24 24 24 8 20 Z"/><circle cx="46" cy="38" r="8" fill="#fff"/><circle cx="46" cy="38" r="4" fill="#e0202f"/></svg>
    BLANKETS
  </div>
  <div class="item" style="left:124px;top:150px;">
    <svg width="80" height="66" viewBox="0 0 80 66"><path fill="none" stroke="#2fa343" stroke-width="4" d="M30 22 V12 C30 4 50 4 50 12 V22"/><path fill="#2fa343" d="M20 20 H60 L62 64 H18 Z"/><circle cx="40" cy="42" r="9" fill="#fff"/><circle cx="40" cy="42" r="4.5" fill="#e0202f"/></svg>
    BAGS
  </div>
  <div class="item" style="left:248px;top:150px;">
    <svg width="80" height="66" viewBox="0 0 80 66"><path fill="none" stroke="#2fa343" stroke-width="4" d="M32 10 C32 2 48 2 48 10"/><path fill="#2fa343" d="M40 8 C58 8 66 20 66 36 V62 H14 V36 C14 20 22 8 40 8 Z"/><circle cx="46" cy="36" r="9" fill="#fff"/><circle cx="46" cy="36" r="4.5" fill="#e0202f"/></svg>
    BACKPACKS
  </div>
  <div class="more" style="left:372px;top:156px;">and<br>many<br>more</div>
</div>

<p class="footer">see all our items at <a href="#">www.beesstitchery-example.com</a></p>

</body>
</html>
```